'Tarvel' a financial/crypto-currency exchange in the middle east

On the card we need 1) Name 2) title 3) email address 4) phone number using the same colors and theme as the logo. On one side we just want the logo and we want the whole card to be in blue (same blue as logo) with the logo in the back being white.
Industry/Entity Type
Financial

```html
<!DOCTYPE html>
<html lang="en">
<head>
<meta charset="UTF-8">
<title>Tarvel Business Card</title>
<link href="https://fonts.googleapis.com/css2?family=Roboto:wght@400;500;700&family=Roboto+Condensed:wght@700&display=swap" rel="stylesheet">
<style>
  :root {
    --backdrop: #2a2b2d;
    --card: #1d1e20;
    --brand-blue: #1c9fd8;
    --name-blue: #27aee6;
    --text-light: #f2f4f5;
    --white: #ffffff;
    --divider: #6a6c70;
  }
  * { margin: 0; padding: 0; box-sizing: border-box; }
  html, body {
    width: 1200px;
    height: 900px;
    overflow: hidden;
    background: var(--backdrop);
  }
  .stage {
    width: 1200px;
    height: 900px;
    display: flex;
    flex-direction: column;
    align-items: center;
    justify-content: center;
    gap: 34px;
  }
  .card {
    width: 700px;
    height: 400px;
    background: var(--card);
    position: relative;
    box-shadow: 0 10px 28px rgba(0, 0, 0, 0.45);
  }

  /* Front side: solid brand blue with white mark */
  .card-front {
    background: var(--brand-blue);
    display: flex;
    flex-direction: column;
    align-items: center;
    justify-content: center;
  }
  .brand {
    display: flex;
    align-items: center;
    gap: 22px;
    margin-top: -20px;
  }
  .brand-circle {
    width: 92px;
    height: 92px;
    border-radius: 50%;
    background: var(--white);
  }
  .brand-name {
    font-family: 'Roboto', sans-serif;
    font-weight: 700;
    font-size: 64px;
    line-height: 1;
    color: var(--white);
    letter-spacing: 1px;
  }
  .front-url {
    margin-top: 58px;
    font-family: 'Roboto', sans-serif;
    font-weight: 400;
    font-size: 15px;
    letter-spacing: 7px;
    color: var(--white);
  }

  /* Back side */
  .card-back {
    display: flex;
    align-items: center;
    justify-content: center;
    padding-top: 40px;
  }
  .identity {
    text-align: right;
    padding-right: 28px;
  }
  .person-name {
    font-family: 'Roboto Condensed', sans-serif;
    font-weight: 700;
    font-size: 36px;
    line-height: 1;
    color: var(--name-blue);
  }
  .person-title {
    margin-top: 4px;
    font-family: 'Roboto', sans-serif;
    font-weight: 500;
    font-size: 17px;
    color: var(--text-light);
    letter-spacing: 0.5px;
  }
  .divider {
    width: 1px;
    height: 76px;
    background: var(--divider);
  }
  .contacts {
    list-style: none;
    padding-left: 28px;
    display: flex;
    flex-direction: column;
    gap: 4px;
  }
  .contact-item {
    display: flex;
    align-items: center;
    gap: 10px;
    font-family: 'Roboto', sans-serif;
    font-weight: 500;
    font-size: 17px;
    color: var(--text-light);
  }
  .contact-icon {
    width: 15px;
    height: 15px;
    fill: var(--brand-blue);
    flex-shrink: 0;
  }
</style>
</head>
<body>
<main class="stage">
  <section class="card card-front">
    <div class="brand">
      <div class="brand-circle"></div>
      <span class="brand-name">Tarvel</span>
    </div>
    <p class="front-url">www.tarvel.com</p>
  </section>

  <section class="card card-back">
    <div class="identity">
      <h1 class="person-name">OMAR HADDAD</h1>
      <p class="person-title">CEO/FOUNDER</p>
    </div>
    <div class="divider"></div>
    <ul class="contacts">
      <li class="contact-item">
        <svg class="contact-icon" viewBox="0 0 24 24" aria-hidden="true">
          <path d="M6.6 10.8c1.4 2.8 3.8 5.1 6.6 6.6l2.2-2.2c.3-.3.7-.4 1-.2 1.1.4 2.3.6 3.6.6.6 0 1 .4 1 1V20c0 .6-.4 1-1 1C10.6 21 3 13.4 3 4c0-.6.4-1 1-1h3.5c.6 0 1 .4 1 1 0 1.3.2 2.5.6 3.6.1.3 0 .7-.2 1l-2.3 2.2z"/>
        </svg>
        <span>555 210 4817</span>
      </li>
      <li class="contact-item">
        <svg class="contact-icon" viewBox="0 0 24 24" aria-hidden="true">
          <path d="M2 5h20v14H2z M4 7v.4l8 5.2 8-5.2V7H4z" fill-rule="evenodd"/>
        </svg>
        <span>omar@tarvel.com</span>
      </li>
      <li class="contact-item">
        <svg class="contact-icon" viewBox="0 0 24 24" aria-hidden="true">
          <circle cx="12" cy="12" r="10"/>
        </svg>
        <span>www.tarvel.com</span>
      </li>
    </ul>
  </section>
</main>
</body>
</html>
```